User profile management app in Bootstrap & AngularJS

We have a single page web app with front end built on AngularJS and Bootstrap. There is a navbar on top and about 10 different views (user profile view, user profile edit, update-able list of items, help section, ...). At this point the app has functionality but no graphics or thought-out layout.

Need a designer to take the existing HTML, CSS (or even JS) files and modify and expand them to make the app look good. Find the existing HTML and JS files for the client attached. You'll need to download angular, bootstrap and ng-map libraries separately.

You can experience the code live at https://design.kelvo.net/kelvoportal.html

The templates provided are text-only but the result should contain a few icons for better visual experience. Some suggested areas for images include device types (email, cell phone, pager, landline phone, ...), status indicators (true/false, on/off, enabled/disabled, ...), navigation (expand/collapse, previous page/next page, ...), file download, CRUD management (add, edit, delete), help popups, etc

The resulting design and code should be mobile-friendly and handicap-accessible (Section 508 compliant).

Font desired: Univers family but not required, otherwise Arial
Only use color from the list provided in the attached file. Colors should not indicate a specific meaning and the whole design should be primarily blue (RGB R0 G103 B198) and white themed.

Allow for banner somewhere on top of page - about 530 x 100 pixels. Allow for a footer with an image on the left and 2-3 sentences of text (copyright, disclaimer, etc).
Updates

Target Market(s)

general public, design for simplicity and ease of use

Industry/Entity Type

Cell Phone

Coding

Coded - Design and coding required

Number of Pages Required

5+ page

Font styles to use
Sans Serif
Other font styles liked:
• Univers family preferred not required otw Arial

Requirements
Must have
• Use blue (RGB R0 G103 B198) and white theme. Must be mobile friendly and handicap-enabled.
• Icons: Use the three stroke weights; light, medium, bold.
• Icons can be designed as outlines or solid silhouettes in two-dimensional form. Icons must be recognizable to a majority of the intended audience. Avoid fine lines and overly complex imagery.

```html
<!DOCTYPE html>
<html lang="en">
<head>
<meta charset="utf-8">
<title>Kelvo Portal – Home</title>
<link rel="stylesheet" href="https://fonts.googleapis.com/css2?family=Arimo:wght@400;700&family=Source+Sans+3:wght@400;600;700&display=swap">
<style>
:root{
  --brand-blue:#0067c6;
  --nav-blue:#016fb3;
  --nav-active:#044a7b;
  --panel-head:#4a4a4a;
  --panel-border:#d5d5d5;
  --table-head:#dff3fc;
  --row-alt:#f4f4f4;
  --text:#444;
  --text-dark:#222;
  --banner-dark:#3a3436;
  --banner-mid:#4a3f36;
  --status-on:#0786cf;
  --status-alias:#f7a832;
  --footer-dark:#1d1d1d;
  --white:#fff;
}
*{margin:0;padding:0;box-sizing:border-box}
html,body{width:1200px;height:828px;overflow:hidden;background:var(--white)}
body{position:relative;font-family:"Source Sans 3",Arial,sans-serif;color:var(--text)}

.site-header{position:absolute;left:0;top:0;width:1200px;height:126px;background:var(--white)}
.brand-name{position:absolute;left:131px;top:40px;font-family:"Arimo",Arial,sans-serif;font-weight:700;font-size:36px;color:var(--brand-blue);letter-spacing:.5px}
.banner{position:absolute;left:542px;top:8px;width:584px;height:110px;background:linear-gradient(90deg,var(--banner-dark) 0%,var(--banner-mid) 60%,var(--banner-dark) 100%)}

.main-nav{position:absolute;left:0;top:126px;width:1200px;height:60px;background:var(--nav-blue)}
.main-nav a{position:absolute;top:13px;height:34px;line-height:34px;font-family:"Arimo",Arial,sans-serif;font-size:18px;color:var(--white);text-decoration:none}
.main-nav a.active{left:105px;width:86px;text-align:center;background:var(--nav-active);border-radius:3px;font-weight:700}

.panel{position:absolute;border:1px solid var(--panel-border);border-radius:5px;background:var(--white);overflow:hidden}
.panel-head{height:55px;background:var(--panel-head);color:var(--white);font-family:"Arimo",Arial,sans-serif;font-weight:700;font-size:18px;display:flex;align-items:center;padding-left:22px;gap:7px}
.panel-head svg{fill:var(--white)}
.profile{left:84px;top:212px;width:490px;height:429px}
.groups{left:596px;top:212px;width:530px;height:186px}
.devices{left:596px;top:421px;width:530px;height:220px}

.profile-list{position:absolute;left:17px;top:80px;width:451px;height:327px;border:1px solid var(--panel-border);border-radius:6px;list-style:none}
.profile-list li{height:45px;border-bottom:1px solid var(--panel-border);display:flex;align-items:center;font-size:16.5px}
.profile-list .label{width:151px;text-align:right;color:var(--text)}
.profile-list .value{padding-left:23px;color:var(--text)}

.data-table{position:absolute;left:10px;width:508px;border-collapse:collapse}
.data-table th{height:44px;background:var(--table-head);text-align:left;font-weight:700;font-size:16.5px;color:var(--text)}
.data-table td{font-size:14.5px;color:var(--text-dark)}
.groups .data-table{top:69px}
.groups th{padding-left:9px}
.groups .col-a,.groups .col-b{width:205px}
.devices .data-table{top:68px}
.devices .col-a{width:218px;padding-left:13px}
.devices .col-b{width:205px}
.data-table .col-c{text-align:center}
.devices tbody tr{height:43px}
.devices tbody tr.first{height:50px}
.devices tbody tr.alt{background:var(--row-alt)}
.status{display:inline-block;width:69px;height:30px;line-height:30px;border-radius:4px;color:var(--white);font-size:14px;text-align:center}
.status-enabled{background:var(--status-on)}
.status-alias{background:var(--status-alias)}

.footer-links{position:absolute;left:0;top:739px;width:1200px;height:32px;background:var(--nav-blue);color:var(--white);font-family:"Arimo",Arial,sans-serif;font-size:13px;line-height:32px;padding-left:86px}
.footer-links a{color:var(--white);text-decoration:none}
.footer-bottom{position:absolute;left:0;top:771px;width:1200px;height:57px;background:var(--footer-dark);color:var(--white);font-family:"Arimo",Arial,sans-serif;font-size:16px;line-height:57px}
.copyright{position:absolute;left:85px}
.support{position:absolute;right:76px}
</style>
</head>
<body>
<header class="site-header">
  <div class="brand-name">Kelvo Portal</div>
  <div class="banner" role="img" aria-label="Banner area: fundraising totals artwork"></div>
</header>

<nav class="main-nav" aria-label="Main">
  <a class="active" href="#">Home</a>
  <a href="#" style="left:212px">Devices</a>
  <a href="#" style="left:313px">Locations</a>
  <a href="#" style="left:428px">Profile</a>
  <a href="#" style="left:517px">Subscriptions</a>
  <a href="#" style="left:662px">Alert Log</a>
  <a href="#" style="left:771px">Help</a>
</nav>

<main>
  <section class="panel profile">
    <h2 class="panel-head">
      <svg width="22" height="24" viewBox="0 0 22 24" aria-hidden="true"><circle cx="11" cy="6.5" r="6"/><path d="M0 24v-4c0-4 4-7 11-7s11 3 11 7v4z"/></svg>
      User Profile
    </h2>
    <ul class="profile-list">
      <li><span class="label">Firstname :</span><span class="value">Owen</span></li>
      <li><span class="label">Last Name :</span><span class="value">Harlow</span></li>
      <li><span class="label">E-mail :</span><span class="value">admin@mailhaven.com</span></li>
      <li><span class="label">City :</span><span class="value">Gotham</span></li>
      <li><span class="label">State :</span><span class="value">American Samoa</span></li>
      <li><span class="label">Languages :</span><span class="value">French , Spanish</span></li>
    </ul>
  </section>

  <section class="panel groups">
    <h2 class="panel-head">
      <svg width="27" height="24" viewBox="0 0 27 24" aria-hidden="true"><circle cx="13.5" cy="5" r="4.5"/><circle cx="5" cy="8" r="3.5"/><circle cx="22" cy="8" r="3.5"/><path d="M6 24v-5c0-3.5 3-6 7.5-6S21 15.5 21 19v5z"/><path d="M0 22v-4c0-2.5 2-4.5 5-4.5 1 0 1.8.2 2.4.5C5.5 15.5 4.5 17.5 4.5 20v2z"/><path d="M27 22v-4c0-2.5-2-4.5-5-4.5-1 0-1.8.2-2.4.5 1.9 1.5 2.9 3.5 2.9 6v2z"/></svg>
      Groups
    </h2>
    <table class="data-table">
      <thead><tr><th class="col-a">Group Name</th><th class="col-b">Category</th><th class="col-c">Type</th></tr></thead>
      <tbody></tbody>
    </table>
  </section>

  <section class="panel devices">
    <h2 class="panel-head">
      <svg width="18" height="26" viewBox="0 0 18 26" aria-hidden="true"><path d="M3 0h12a3 3 0 0 1 3 3v20a3 3 0 0 1-3 3H3a3 3 0 0 1-3-3V3a3 3 0 0 1 3-3zm0 4v16h12V4zm6 17.5a1.5 1.5 0 1 0 0 3 1.5 1.5 0 0 0 0-3z"/></svg>
      Devices
    </h2>
    <table class="data-table">
      <thead><tr><th class="col-a">Device Identifier</th><th class="col-b">Delivery Channel</th><th class="col-c">Status</th></tr></thead>
      <tbody>
        <tr class="first"><td class="col-a">oharlow@ledgerly.com</td><td class="col-b">E-mail account</td><td class="col-c"><span class="status status-enabled">Enabled</span></td></tr>
        <tr class="alt"><td class="col-a">Owl-note@ledgerly.com</td><td class="col-b">E-mail account</td><td class="col-c"><span class="status status-alias">Alias</span></td></tr>
      </tbody>
    </table>
  </section>
</main>

<footer>
  <div class="footer-links">Important links : <a href="#">Home</a> &nbsp;|&nbsp; <a href="#">Devices</a> &nbsp;|&nbsp; <a href="#">Locations</a> &nbsp;|&nbsp; <a href="#">Profile</a> &nbsp;|&nbsp; <a href="#">Subscriptions</a> &nbsp;|&nbsp; <a href="#">Alert Log</a> &nbsp;|&nbsp; <a href="#">About us</a> &nbsp;|&nbsp; <a href="#">Contact us</a> &nbsp;!&nbsp; <a href="#">Help</a></div>
  <div class="footer-bottom">
    <span class="copyright">CopyRight @ Kelvo.net 2015</span>
    <span class="support">Contact Support : support@kelvo.net</span>
  </div>
</footer>
</body>
</html>
```